Web Design Project

We need a web design for a new company that we started called ZARN CNG. ZARN CNG is a company that will build, own and operate compressed natural gas fueling stations throughout the United States. Our primary customers are Trucking companies and the stations will be built for semi trucks. CNG is better for the environment than diesel fuel, and will save trucking companies loads of money. It is also a domestic product which means that it will create American jobs and help America become energy independent. I have attached a logo that we are using. We dont need to stay with this logo persay, but it is what we have for now. We have a video on Vidlo that shows a bit of what we are doing. just search for ZARN CNG. ZARN CNG is a sister company of Holtmark of Arizona,www.hkqvz.example and a nationwide distributor of TRIVEX FUEL, www.trivexfuel.example. We will need links to these sites. Please make any pictures of trucks Holtmark trucks, and please do not use pictures of cabover trucks.

Target Market(s)

The target market are truck drivers and truckers.

Industry/Entity Type

Environment

Requirements
Must have
• Map showing station locations, a page with industry news, a page with a savings calculator (we can code the calculator) Site should have links to

```html
<!DOCTYPE html>
<html lang="en">
<head>
<meta charset="utf-8">
<title>ZARN CNG</title>
<link rel="stylesheet" href="https://fonts.googleapis.com/css2?family=Arimo:wght@400;700&family=Open+Sans:wght@400&display=swap">
<style>
:root{
  --teal:#18b7c2;
  --teal-dark:#0f9aa6;
  --teal-text:#1a9fb0;
  --green:#2ecc40;
  --text:#555;
  --muted:#777;
  --panel:#ececec;
  --footer:#4a4a4a;
}
*{margin:0;padding:0;box-sizing:border-box}
html,body{width:1150px;height:1200px;overflow:hidden}
body{position:relative;font-family:Arimo,Arial,sans-serif;color:var(--text);background:linear-gradient(#e9e9e9 0,#f6f6f6 500px,#fff 940px,#fff 100%)}
.abs{position:absolute}
.topbar{left:0;top:0;width:1150px;height:43px;background:linear-gradient(90deg,#20b8c8,#34cde0 50%,#22bccb)}
.account{left:748px;top:12px;font-size:14px;color:#fff;text-shadow:0 1px 1px #333}
.account span{margin:0 10px}
.search{left:897px;top:8px;width:166px;height:24px;background:#fff;border:1px solid #ccc;border-radius:2px;font-size:11px;font-style:italic;color:#999;padding:5px 14px}
.brand{left:88px;top:58px;display:flex;align-items:center;gap:8px;font-size:34px;font-weight:700;color:var(--green);white-space:nowrap}
.brand i{display:block;width:12px;height:12px;border-radius:50%;background:var(--green)}
.nav{left:533px;top:68px;width:528px;height:47px;background:linear-gradient(#22c1c9,#13a8b2);display:flex}
.nav a{color:#fff;text-decoration:none;font-size:14px;line-height:45px;text-align:center;border-right:1px solid rgba(0,0,0,.12)}
.nav a.active{background:linear-gradient(#1aa69c,#0d8c86)}
.panel{left:86px;top:115px;width:978px;height:820px;background:#fff;border-top:4px solid var(--teal-dark);box-shadow:0 1px 3px rgba(0,0,0,.15)}
.slider{left:93px;top:127px;width:964px;height:323px;background:#ddd}
.slide{left:100px;top:134px;width:950px;height:309px;background:#0b0b0b}
.photo{left:100px;top:134px;width:390px;height:309px;background:linear-gradient(100deg,#7b7d7a,#a9aba6 45%,#3a3d3f 80%,#0b0b0b)}
.tagline{left:502px;top:214px;width:242px;font-size:17px;line-height:28px;color:#fff;text-align:justify}
.dots{left:646px;top:408px;display:flex;gap:20px}
.dots i{width:10px;height:10px;border-radius:50%;background:#1ac3d6}
.dots i:first-child{background:var(--green)}
.calc{left:775px;top:151px;width:253px;height:272px;background:#fff;border:3px solid #e4e4e4}
.calc h3{font-weight:400;font-size:18px;color:var(--teal-text);padding:10px 14px 8px;border-bottom:1px solid #e6e6e6;margin:0 4px;white-space:nowrap}
.row{position:absolute;left:17px;font-size:12px;color:#444}
.select{position:absolute;left:120px;width:117px;height:28px;border:1px solid #ccc;border-radius:2px;font-size:11px;font-style:italic;color:#888;display:flex;align-items:center}
.select b{width:60px;padding-left:10px;font-weight:400}
.select em{border-left:1px solid #ddd;padding-left:5px;width:45px}
.select:after{content:"";border:4px solid transparent;border-top-color:#555;margin-top:4px}
.result{position:absolute;left:3px;top:186px;width:186px;height:74px;background:#f6fbfb;border:1px solid #e1eeee;font-size:11.5px;color:var(--teal-dark);padding:7px 10px;line-height:18px;white-space:nowrap;overflow:hidden}
.result span{display:block}
.result .metric{padding-left:80px}
.result .cost{margin-top:6px}
.calc-art{left:966px;top:333px;width:70px;height:92px;border-radius:8px;background:linear-gradient(#f4f4f4,#b9bcbc)}
h2.title{position:absolute;font-weight:400;color:var(--teal-text)}
.copy{position:absolute;font-size:13px;line-height:22px;text-align:justify;color:var(--text)}
.dotted{left:96px;top:646px;width:650px;border-top:2px dotted #aaa}
.benefit{position:absolute;top:796px;width:198px}
.benefit .head{display:flex;align-items:center;gap:10px;height:42px;border-bottom:1px solid #ddd;font-size:18px;color:var(--teal-text);white-space:nowrap}
.benefit .ico{width:56px;height:32px;border-radius:3px;flex:none}
.benefit p{font-size:12px;line-height:20px;margin-top:10px;color:#555;text-align:justify}
.loc-head{left:775px;top:476px;display:flex;align-items:center;gap:10px;font-size:18px;color:var(--teal-text)}
.finder{left:773px;top:518px;width:282px;height:257px;background:var(--panel);border-radius:3px}
.finder label{position:absolute;left:10px;top:23px;font-size:12px;color:#444}
.finder .field{position:absolute;left:112px;top:15px;width:163px;height:28px;background:#fff;border:1px solid #ccc}
.finder .btn{position:absolute;left:182px;top:50px;width:92px;height:24px;background:linear-gradient(#2fc2cf,#1398a6);color:#fff;font-size:11px;text-align:center;line-height:24px;border-radius:2px}
.map{position:absolute;left:7px;top:92px;width:268px;height:159px;background:linear-gradient(135deg,#ecebe3,#dcdbd0);border:1px solid #ccc}
.usage{left:773px;top:785px;width:282px;height:125px;background:linear-gradient(#3fd0d8,#15aab6);border:1px solid #12a0ad;border-radius:3px;color:#fff}
.usage .truck{position:absolute;left:18px;top:10px;width:46px;height:36px;background:linear-gradient(#f39c26,#333);border-radius:3px}
.usage h3{position:absolute;left:75px;top:10px;font-size:16px;font-weight:700;width:188px;padding-bottom:10px;border-bottom:1px solid rgba(255,255,255,.8);white-space:nowrap}
.usage p{position:absolute;left:20px;top:54px;width:243px;font-size:13px;line-height:18px;text-align:justify}
.sep{left:86px;top:951px;width:980px;border-top:1px solid #ddd}
.fcol{position:absolute;top:976px;font-size:12px;color:var(--muted)}
.fcol h4{font-size:13px;font-weight:400;color:var(--teal-text);margin-bottom:9px}
.fcol li{list-style:none;line-height:18px;padding-left:14px;position:relative}
.fcol li:before{content:"";position:absolute;left:1px;top:6px;width:5px;height:5px;border-top:1.5px solid #666;border-right:1.5px solid #666;transform:rotate(45deg)}
.vline{left:817px;top:978px;height:108px;border-left:1px solid #ddd}
.news-head{left:848px;top:975px;display:flex;align-items:center;gap:12px;font-size:14px;color:var(--teal-text);white-space:nowrap}
.news-input{left:846px;top:1008px;width:154px;height:27px;border:1px solid #ccc;background:#fff;font-size:12px;font-style:italic;color:#777;padding:6px 11px}
.news-btn{left:1004px;top:1008px;width:59px;height:27px;background:#555;color:#fff;font-size:12px;font-style:italic;text-align:center;line-height:27px}
.news-note{left:849px;top:1051px;width:210px;font-size:12px;line-height:18px;color:#888}
.footer{left:0;top:1121px;width:1150px;height:79px;background:var(--footer);font-family:"Open Sans",Arial,sans-serif;font-size:11px;color:#ddd}
.footer .links{position:absolute;left:94px;top:18px}
.footer .links span{margin:0 6px;color:#aaa}
.footer .legal{position:absolute;left:94px;top:48px}
.social{position:absolute;top:27px;width:28px;height:28px;border-radius:50%;background:#fff;color:#1b7fc1;font-size:6px;text-align:center;line-height:28px;overflow:hidden;white-space:nowrap}
</style>
</head>
<body>
<div class="abs topbar"></div>
<div class="abs account">Sign in<span>|</span>Register</div>
<div class="abs search">Search</div>

<div class="abs brand">ZARN CNG<i></i></div>
<nav class="abs nav">
  <a class="active" style="width:70px">Home</a><a style="width:64px">About</a><a style="width:80px">Services</a><a style="width:84px">Solutions</a><a style="width:88px">Locations</a><a style="width:62px">News</a><a style="width:80px;border:0">Contact</a>
</nav>

<div class="abs panel"></div>
<div class="abs slider"></div>
<div class="abs slide"></div>
<div class="abs photo" role="img" aria-label="Photo of a CNG fuel nozzle connected to a truck tank"></div>
<p class="abs tagline">Compressed Natural Gas is more economic on money and better than diesel and more safe to the ecology.</p>
<div class="abs dots"><i></i><i></i><i></i><i></i></div>

<div class="abs calc">
  <h3>Money Saving Calcualtor</h3>
  <div class="row" style="top:64px">Distance Driven :</div>
  <div class="select" style="top:55px"><b>357</b><em>Miles</em></div>
  <div class="row" style="top:105px">Gas Used :</div>
  <div class="select" style="top:96px"><b>18.5</b><em>Galns</em></div>
  <div class="row" style="top:146px">Price of Gas :</div>
  <div class="select" style="top:137px"><b>4.22</b><em>Dollar</em></div>
  <div class="result"><span>Gas Mileage : 19.3 MPG</span><span class="metric">12.19 L/100km</span><span class="cost">Cost / Distance : $0.22 / Mile</span></div>
</div>
<div class="abs calc-art" role="img" aria-label="Pocket calculator illustration"></div>

<h2 class="title" style="left:96px;top:476px;font-size:22px">Welcome to our site</h2>
<p class="copy" style="left:96px;top:514px;width:648px">Mauris pretium interdum velit non ultrices. Cras a cursus magna. Phasellus facilisis dignissim augue vel consectetur. Nunc commodo tincidunt purus eu posuere. Sed blandit faucibus nibh eget rutrum. Nam purus arcu, eleifend vulputate hendrerit nec, scelerisque ut erat. Maecenas rhoncus ultrices nisl. Sed elementum sollicitudin volutpat. Phasellus pharetra elit euismod ligula lobortis sit amet convallis velit placerat. Ut pellentesque pellentesque arcu et eleifend. Curabitur euismod libero sit amet sapien ultrices mollis.</p>
<div class="abs dotted"></div>
<h2 class="title" style="left:95px;top:675px;font-size:18px">Benefits of CNG</h2>
<p class="copy" style="left:96px;top:708px;width:648px">Nam purus arcu, eleifend vulputate hendrerit nec, scelerisque ut erat. Maecenas rhoncus ultrices nisl. Sed elementum sollicitudin volutpat. Phasellus pharetra elit euismod ligula lobortis sit amet convallis velit placerat. Ut pellentesque pellentesque arcu et eleifend. Curabitur euismod libero sit amet sapien ultrices mollis.</p>

<div class="benefit" style="left:94px">
  <div class="head"><div class="ico" style="background:linear-gradient(#9bc88a,#4f7a46)" role="img" aria-label="Banknotes illustration"></div>More Economic</div>
  <p>Pellentesque accumsan ipsum sed augue faucibus eleimorbi elementum eros id ipsum auctor vitae</p>
</div>
<div class="benefit" style="left:321px">
  <div class="head"><svg width="30" height="32" viewBox="0 0 30 32"><rect x="4" y="3" width="14" height="26" rx="2" fill="#17aab6"/><rect x="7" y="7" width="8" height="6" fill="#fff"/><path d="M18 10h4l3 4v10a2 2 0 0 1-4 0v-6h-3" fill="none" stroke="#17aab6" stroke-width="2"/><rect x="2" y="28" width="18" height="3" fill="#17aab6"/></svg>Better than diesel</div>
  <p>Pellentesque accumsan ipsum sed augue faucibus eleimorbi elementum eros id ipsum auctor vitae</p>
</div>
<div class="benefit" style="left:548px">
  <div class="head"><div class="ico" style="width:30px;background:linear-gradient(#9ed14a,#4d9a2c)" role="img" aria-label="Green sprout illustration"></div>Safe to the Ecology</div>
  <p>Pellentesque accumsan ipsum sed augue faucibus eleimorbi elementum eros id ipsum auctor vitae</p>
</div>

<div class="abs loc-head"><svg width="14" height="26" viewBox="0 0 14 26"><path d="M7 0a7 7 0 0 1 7 7c0 5-7 19-7 19S0 12 0 7a7 7 0 0 1 7-7z" fill="#1a7fc4"/><circle cx="7" cy="7" r="3" fill="#fff"/></svg>Available locations</div>
<div class="abs finder">
  <label>Enter Your Area :</label>
  <div class="field"></div>
  <div class="btn">Search Station</div>
  <div class="map" role="img" aria-label="Street map showing nearby CNG station"></div>
</div>

<div class="abs usage">
  <div class="truck" role="img" aria-label="Delivery truck illustration"></div>
  <h3>CNG Usage on Vehicles</h3>
  <p>Phasellus pharetra elit euismod ligula lobortis sit amet convallis velit placerat euismod libero sapien ultrices.</p>
</div>

<div class="abs sep"></div>
<div class="fcol" style="left:94px"><h4>About us</h4><ul><li>Consectetur</li><li>Mauris ideaui</li><li>Aunc vivera ornare</li><li>Nunc convallis</li><li>Nulla faucibusodio</li></ul></div>
<div class="fcol" style="left:275px"><h4>Services</h4><ul><li>Consectetur</li><li>Mauris ideaui</li><li>Aunc vivera ornare</li><li>Nunc convallis</li><li>Nulla faucibusodio</li></ul></div>
<div class="fcol" style="left:465px"><h4>Solutions</h4><ul><li>Consectetur</li><li>Mauris ideaui</li><li>Aunc vivera ornare</li><li>Nunc convallis</li><li>Nulla faucibusodio</li></ul></div>
<div class="fcol" style="left:646px"><h4>Cities</h4><ul><li>Consectetur</li><li>Mauris ideaui</li><li>Aunc vivera ornare</li><li>Nunc convallis</li><li>Nulla faucibusodio</li></ul></div>
<div class="abs vline"></div>
<div class="abs news-head"><svg width="18" height="16" viewBox="0 0 18 16"><rect x="0" y="3" width="18" height="13" fill="#7cb3e0"/><path d="M0 3l9 7 9-7" fill="none" stroke="#fff" stroke-width="1.5"/><rect x="4" y="0" width="10" height="6" fill="#f3c542"/></svg>NEWSLETTER SUBSCRIBE</div>
<div class="abs news-input">Enter your E-mail ID</div>
<div class="abs news-btn">SUBMIT</div>
<p class="abs news-note">Quis autem vel eum iure reprehenderit qui in ea voluptate velit esse</p>

<footer class="abs footer">
  <div class="links">Home<span>|</span>About<span>|</span>Services<span>|</span>Solutions<span>|</span>Locations<span>|</span>News<span>|</span>Contact</div>
  <div class="legal">Copyright © 2012 www.zarncng.example &nbsp;&nbsp; All rights reserved.</div>
  <div class="social" style="left:992px">Facenet</div>
  <div class="social" style="left:1028px">Chirpline</div>
</footer>
</body>
</html>
```